The Wattlebrook Pup Parlour

I have a logo which I designed myself ( I tried a contest and it did not work out well..not on this site) The logo needs some tweaking for example "THE" needs to be put above "WATTLEBROOK" in line with the D (on top)and it needs to be going across sideways.Also the dog is not exactly in the middle.
Also on the card I would like my name written in a simple running writing script
Heather

Then in plain writing:
27B Harlan St Corrowin NSW 2794
Ph. 6381 5907
On the back:
Your next appointment:
...........................................

Pet bathing, clipping and styling

Industry/Entity Type

Pet

Requirements
Must have
• The logo going across lengthways and changed a bit (as explained above)

```html
<!DOCTYPE html>
<html lang="en">
<head>
<meta charset="utf-8">
<title>The Wattlebrook Pup Parlour — Business Card</title>
<link rel="stylesheet" href="https://fonts.googleapis.com/css2?family=Cabin:wght@400;700&family=Norican&display=swap">
<style>
  :root {
    --backdrop: #2a2b2e;
    --card: #f1f1f0;
    --ink: #1c1c1c;
    --accent-red: #d0202a;
    --poodle-light: #dbe6ee;
    --poodle-mid: #b9cad8;
    --bubble-fill: #d6e0e8;
    --bubble-edge: #4a5560;
  }
  * { box-sizing: border-box; margin: 0; padding: 0; }
  html, body {
    width: 1200px;
    height: 984px;
    overflow: hidden;
    background: var(--backdrop);
  }
  .stage {
    position: relative;
    width: 1200px;
    height: 984px;
  }
  .card {
    position: absolute;
    left: 220px;
    width: 760px;
    height: 434px;
    background: var(--card);
    border-radius: 4px;
    overflow: hidden;
  }
  .card--back { top: 40px; }
  .card--front { top: 510px; }

  /* Back side */
  .appointment-bubble {
    position: absolute;
    left: 40px;
    top: 70px;
    width: 400px;
    height: 140px;
  }
  .appointment-label {
    position: absolute;
    left: 76px;
    top: 100px;
    font-family: 'Cabin', sans-serif;
    font-size: 23px;
    color: var(--ink);
    white-space: nowrap;
  }
  .appointment-line {
    position: absolute;
    left: 76px;
    top: 168px;
    width: 300px;
    border-bottom: 3px dotted var(--ink);
  }
  .poodle-art {
    position: absolute;
    border-radius: 48% 48% 40% 40%;
    background: radial-gradient(circle at 50% 45%, var(--poodle-light), var(--poodle-mid));
  }
  .card--back .poodle-art {
    left: 470px;
    top: 24px;
    width: 250px;
    height: 290px;
  }
  .services-line {
    position: absolute;
    left: 40px;
    top: 372px;
    font-family: 'Norican', cursive;
    font-size: 26px;
    color: var(--ink);
    white-space: nowrap;
  }

  /* Front side */
  .brand {
    position: absolute;
    left: 44px;
    top: 96px;
    display: flex;
    align-items: center;
    gap: 14px;
    white-space: nowrap;
  }
  .brand-dot {
    width: 18px;
    height: 18px;
    border-radius: 50%;
    background: var(--accent-red);
  }
  .brand-name {
    font-family: 'Cabin', sans-serif;
    font-weight: 700;
    font-size: 34px;
    color: var(--ink);
  }
  .card--front .poodle-art {
    left: 600px;
    top: 26px;
    width: 130px;
    height: 150px;
  }
  .holder-name {
    position: absolute;
    left: 48px;
    top: 232px;
    font-family: 'Norican', cursive;
    font-size: 58px;
    color: var(--ink);
    white-space: nowrap;
  }
  .divider {
    position: absolute;
    left: 282px;
    top: 228px;
    width: 3px;
    height: 160px;
    background: linear-gradient(to bottom, rgba(28,28,28,0), var(--ink) 40%, var(--ink) 70%, rgba(28,28,28,0));
  }
  .contact {
    position: absolute;
    left: 306px;
    top: 262px;
    list-style: none;
    font-family: 'Cabin', sans-serif;
    font-size: 25px;
    color: var(--ink);
  }
  .contact li {
    display: flex;
    align-items: center;
    gap: 12px;
    margin-bottom: 14px;
    white-space: nowrap;
  }
  .contact svg { width: 24px; height: 24px; flex: none; }
</style>
</head>
<body>
<main class="stage">

  <section class="card card--back" aria-label="Card back">
    <svg class="appointment-bubble" viewBox="0 0 400 140" aria-hidden="true">
      <path d="M16 4 H350 Q364 4 364 18 V96 L396 116 L340 112 Q334 122 322 122 H16 Q4 122 4 110 V18 Q4 4 16 4 Z"
            fill="var(--bubble-fill)" stroke="var(--bubble-edge)" stroke-width="3"/>
    </svg>
    <p class="appointment-label">Your next appointment:</p>
    <div class="appointment-line"></div>
    <div class="poodle-art" role="img" aria-label="Cartoon illustration of a fluffy white poodle"></div>
    <p class="services-line">Pet bathing, clipping and styling</p>
  </section>

  <section class="card card--front" aria-label="Card front">
    <div class="brand">
      <span class="brand-dot"></span>
      <span class="brand-name">The Wattlebrook Pup Parlour</span>
    </div>
    <div class="poodle-art" role="img" aria-label="Cartoon illustration of a fluffy white poodle"></div>
    <p class="holder-name">Heather</p>
    <div class="divider"></div>
    <ul class="contact">
      <li>
        <svg viewBox="0 0 24 24" aria-hidden="true">
          <path d="M12 3 L2 12 H5 V21 H10 V15 H14 V21 H19 V12 H22 Z" fill="var(--accent-red)"/>
        </svg>
        <span>27B Harlan St Corrowin NSW 2794</span>
      </li>
      <li>
        <svg viewBox="0 0 24 24" aria-hidden="true">
          <path d="M6.6 10.8 a15 15 0 0 0 6.6 6.6 l2.2-2.2 a1 1 0 0 1 1-.25 a11.4 11.4 0 0 0 3.6.57 a1 1 0 0 1 1 1 V20 a1 1 0 0 1-1 1 A17 17 0 0 1 3 4 a1 1 0 0 1 1-1 h3.5 a1 1 0 0 1 1 1 a11.4 11.4 0 0 0 .57 3.6 a1 1 0 0 1-.25 1 Z" fill="var(--accent-red)"/>
        </svg>
        <span>6381 5907</span>
      </li>
    </ul>
  </section>

</main>
</body>
</html>
```